Business Card/ Email Signature Design Project

I am an Interior Designer. I need a business card that looks sophisticated stylish but simple in design. My work covers space design/ interior architecture/ furniture design/ product development & styling.

I have a very specific brief and know mostly what I want. I'm hoping to work with someone who can translate my ideas.

My branding should have a strong focus on my name, the majority of my work is referral based.
I'm keen to keep a monochromatic colour scheme: dark charcoal/ black/ white/ embossing/ silver. I'm not suggesting we use all that I've listed, they are possible ideas at this stage. I will need to be mindful of printing costs an also how I make the design work across, cards, letter heads, email logo and web design.

Theory behind images sent below;
1-Rug Image_(minus boarder) I was thinking this image could be used on the back of the card with my contact details over. I like that the lines are almost hand drawn and start to look free form. It's a subtle contrast to a more formal front of the card with my name.
2_Owen Ratley_I really like the orientation, the proportion of font on the card, the colour and the font. I like the lower case for my name and the upper case for 'Interior Design'. Not sure if it should be 'Interior Designer or Interior Design' at this stage, was leaning towards 'Interior Design'. Was thinking the 'i' and 'd' in my surname could be the colour eg 'silver'?? We can decide on this once we see it.

Look forward to hearing from you.
Cheers,
Noreen Bastoli

Industry/Entity Type

Printing

Logo Text

Noreen Bastoli Interior Design

```html
<!DOCTYPE html>
<html lang="en">
<head>
<meta charset="utf-8">
<title>Noreen Bastoli Interior Design – Business Card</title>
<link rel="stylesheet" href="https://fonts.googleapis.com/css2?family=Roboto:wght@400;700&display=swap">
<style>
  :root {
    --backdrop: #e9e7e4;
    --charcoal: #262626;
    --white: #ffffff;
    --ink: #1c1c1c;
    --icon: #7a7a7a;
    --rug-light: #dcdad6;
    --rug-mid: #c9c6c1;
    --rug-dark: #b5b2ad;
  }
  * { box-sizing: border-box; margin: 0; padding: 0; }
  html, body {
    width: 1200px;
    height: 1000px;
    overflow: hidden;
    background: var(--backdrop);
    font-family: "Roboto", Arial, sans-serif;
  }
  .sheet {
    position: relative;
    width: 1200px;
    height: 1000px;
  }
  .card {
    position: absolute;
    left: 235px;
    width: 730px;
    height: 415px;
    overflow: hidden;
  }
  .card--front {
    top: 60px;
    background: var(--charcoal);
    display: flex;
    align-items: center;
    justify-content: center;
  }
  .card--back { top: 525px; }

  .brand-name {
    font-weight: 400;
    line-height: 1.2;
    white-space: nowrap;
  }
  .card--front .brand-name {
    font-size: 56px;
    color: var(--white);
    text-align: center;
  }
  .card--front .brand-name span { display: block; font-size: 30px; }

  .rug-surface {
    position: absolute;
    inset: 0;
    background: linear-gradient(160deg, var(--rug-light) 0%, var(--rug-mid) 55%, var(--rug-dark) 100%);
  }
  .card--back .brand-name {
    position: absolute;
    top: 44px;
    right: 30px;
    font-size: 28px;
    color: var(--ink);
    text-align: right;
  }
  .card--back .brand-name span { display: block; font-size: 16px; }

  .contact-list {
    position: absolute;
    left: 20px;
    bottom: 60px;
    list-style: none;
  }
  .contact-list__item {
    display: flex;
    align-items: center;
    height: 24.5px;
    font-size: 13px;
    font-weight: 700;
    letter-spacing: 0.2em;
    color: var(--ink);
    white-space: nowrap;
  }
  .contact-list__icon {
    width: 16px;
    height: 16px;
    margin-right: 27px;
    fill: var(--icon);
    flex: none;
  }
</style>
</head>
<body>
<main class="sheet">

  <section class="card card--front" aria-label="Business card front">
    <div class="brand-name">Noreen Bastoli<span>Interior Design</span></div>
  </section>

  <section class="card card--back" aria-label="Business card back">
    <div class="rug-surface" role="img" aria-label="Close-up photograph of a pale woven rug with freehand black geometric lines"></div>

    <div class="brand-name">Noreen Bastoli<span>Interior Design</span></div>

    <ul class="contact-list">
      <li class="contact-list__item">
        <svg class="contact-list__icon" viewBox="0 0 16 16" aria-hidden="true">
          <path d="M3 1h10a1 1 0 0 1 1 1v12a1 1 0 0 1-1 1H3a1 1 0 0 1-1-1V2a1 1 0 0 1 1-1zm1 2v8h8V3H4zm4 9.2a.9.9 0 1 0 0 1.8.9.9 0 0 0 0-1.8z"/>
        </svg>
        0400 555 218
      </li>
      <li class="contact-list__item">
        <svg class="contact-list__icon" viewBox="0 0 16 16" aria-hidden="true">
          <path d="M1 2h14v12H1V2zm1.5 3v7.5h11V5h-11zM3 3a.6.6 0 1 0 0 1.2A.6.6 0 0 0 3 3zm1.8 0a.6.6 0 1 0 0 1.2.6.6 0 0 0 0-1.2z"/>
        </svg>
        www.noreenbastoli.com
      </li>
      <li class="contact-list__item">
        <svg class="contact-list__icon" viewBox="0 0 16 16" aria-hidden="true">
          <path d="M1 3h14v10H1V3zm1.4 1.2L8 8.6l5.6-4.4H2.4zM2.2 5.5v6.3h11.6V5.5L8 10 2.2 5.5z"/>
        </svg>
        interiors@noreenbastoli.com
      </li>
      <li class="contact-list__item">
        <svg class="contact-list__icon" viewBox="0 0 16 16" aria-hidden="true">
          <path d="M8 1.5 15 7.5h-2V14H3V7.5H1L8 1.5zm-2 8V14h4V9.5H6z"/>
        </svg>
        P.O Box 512 Fernmont VIC. 3990
      </li>
    </ul>
  </section>

</main>
</body>
</html>
```